Website redesign

Redesign the Website

http://www.trauringe-kolbeck.de/

Task

- make 1 Layout for the Website
- Colors: white, yellow, brown
- Text: Take from Page - ore rather Use Latin - Lore Ipsum ...
- pimp design and overall look
- enhance overview for better orientation
- more freindly / sympatic overall look.
- Better integrate Palvista Button aso.
- send Layout as layered PSD

```html
<!DOCTYPE html>
<html lang="de">
<head>
<meta charset="utf-8">
<title>Trauringe Kolbeck</title>
<link href="https://fonts.googleapis.com/css2?family=Great+Vibes&family=Playfair+Display:ital,wght@1,400;1,600&family=Open+Sans:wght@400;600;700&display=swap" rel="stylesheet">
<style>
:root{
  --gold:#e8b923;
  --gold-dark:#c89a14;
  --brown:#5a2a17;
  --brown-dark:#3f1c0f;
  --text:#4a4a4a;
  --muted:#8a8a8a;
  --bg:#f3f3f3;
  --card:#ffffff;
  --line:#dcdcdc;
  --footer:#2b2b2b;
  --footer-bar:#1f1f1f;
}
*{margin:0;padding:0;box-sizing:border-box}
html,body{width:1200px;height:2984px;overflow:hidden}
body{font-family:"Open Sans",Arial,sans-serif;color:var(--text);background:var(--bg);font-size:13px}
.site-header{height:160px;background:#fff;display:flex;align-items:center;padding:0 100px;justify-content:space-between;border-bottom:1px solid var(--line)}
.brand{display:flex;align-items:center;gap:12px;font-family:"Open Sans",Arial,sans-serif;font-weight:700;font-size:24px;letter-spacing:1px;color:var(--brown);line-height:1.05}
.brand-dot{width:14px;height:14px;border-radius:50%;background:var(--gold)}
.main-nav{display:flex;align-items:center;gap:38px;font-size:14px}
.main-nav a{color:var(--text);text-decoration:none}
.main-nav a.active{color:var(--gold-dark)}
.search-btn{width:44px;height:44px;background:var(--gold);display:flex;align-items:center;justify-content:center}
.hero{position:relative;height:640px;background:linear-gradient(115deg,#3b3b3b 0%,#8d8d8d 35%,#cfcfcf 55%,#6e6e6e 80%,#2e2e2e 100%)}
.hero-title{position:absolute;left:110px;top:200px;font-family:"Great Vibes",cursive;font-size:64px;color:#fff}
.hero-note{position:absolute;left:690px;top:440px;font-family:"Great Vibes",cursive;font-size:38px;line-height:1.25;color:var(--gold)}
.hero-arrow{position:absolute;top:300px;width:34px;height:34px;border-radius:50%;background:rgba(0,0,0,.45);display:flex;align-items:center;justify-content:center}
.hero-arrow.prev{left:30px}.hero-arrow.next{right:30px}
.container{width:980px;margin:0 auto}
.info{padding:60px 0 10px}
.section-title{font-family:"Playfair Display",serif;font-style:italic;font-weight:600;font-size:30px;color:var(--brown);text-align:center}
.title-rule{width:90px;height:2px;background:var(--gold);margin:10px auto 30px}
.info-row{display:flex;gap:40px;align-items:flex-start}
.info-row p{flex:1;line-height:1.7;font-size:12px;color:var(--muted)}
.partner-badge{width:170px;height:90px;border:1px solid var(--line);background:#fff}
.edition-title{font-family:"Playfair Display",serif;font-style:italic;font-weight:600;font-size:30px;color:var(--brown);margin:50px 0 6px}
.edition-rule{height:1px;background:var(--line);margin-bottom:30px}
.card-grid{display:grid;grid-template-columns:repeat(3,300px);gap:40px}
.ring-card{background:var(--card);box-shadow:0 2px 8px rgba(0,0,0,.15);height:280px;display:flex;flex-direction:column;align-items:center}
.ring-photo{width:100%;height:150px}
.photo-gold{background:radial-gradient(circle at 50% 55%,#f4d46a 0%,#e2b53a 35%,#fafafa 70%)}
.photo-bicolor{background:radial-gradient(circle at 50% 55%,#e9d49a 0%,#cfcfcf 40%,#fafafa 72%)}
.photo-white{background:radial-gradient(circle at 50% 55%,#d6d6d6 0%,#b8b8b8 35%,#fafafa 72%)}
.ring-specs{list-style:none;font-size:11px;color:var(--text);text-align:center;padding:14px 18px 0;line-height:1.7;flex:1}
.ring-specs li{display:inline-block;margin:0 5px}
.ring-specs li::before{content:"✓ ";color:var(--gold-dark)}
.btn-request{background:var(--brown);color:#fff;font-size:11px;padding:8px 26px;margin-bottom:22px;border-radius:2px}
.design-banner{margin-top:60px;height:300px;position:relative;background:linear-gradient(90deg,#3a322c,#6b5f55 45%,#2c2622);box-shadow:0 2px 8px rgba(0,0,0,.2)}
.banner-text{position:absolute;left:40px;top:60px;width:380px;color:#f1f1f1}
.banner-text h3{font-family:"Playfair Display",serif;font-style:italic;font-weight:400;font-size:28px;margin-bottom:16px}
.banner-text p{font-size:11px;line-height:1.6;margin-bottom:18px}
.banner-video{position:absolute;right:30px;top:40px;width:470px;height:220px;background:linear-gradient(135deg,#d9d9d9,#9a9a9a);border:4px solid #1e1e1e}
.site-footer{margin-top:140px;background:var(--footer);height:240px;padding:40px 100px 0;display:flex;gap:60px}
.footer-brand{width:230px}
.footer-brand .brand{color:#fff;font-size:20px}
.social-btn{margin-top:70px;width:150px;height:30px;background:#3b5a9a;color:#fff;font-size:12px;display:flex;align-items:center;padding-left:14px}
.footer-col{list-style:none;width:200px;color:#cfcfcf;font-size:13px;line-height:2.2}
.footer-bar{background:var(--footer-bar);height:44px;color:#9a9a9a;font-size:11px;display:flex;align-items:center;justify-content:center}
</style>
</head>
<body>
<header class="site-header">
  <div class="brand"><span class="brand-dot"></span><span>TRAURINGE<br>KOLBECK.DE</span></div>
  <nav class="main-nav">
    <a class="active" href="#">Trauringe</a><a href="#">Gebäringe</a><a href="#">Partnerringe</a><a href="#">Brautschmuck</a><a href="#">Informationen</a><a href="#">Kontakt</a>
    <span class="search-btn"><svg width="18" height="18" viewBox="0 0 18 18"><circle cx="7.5" cy="7.5" r="5.5" fill="none" stroke="#fff" stroke-width="2"/><line x1="11.5" y1="11.5" x2="16" y2="16" stroke="#fff" stroke-width="2"/></svg></span>
  </nav>
</header>

<section class="hero" role="img" aria-label="Schwarzweißfoto eines Brautpaares mit Verlobungsring an der Hand">
  <div class="hero-title">Ihr Weg zum Glück...</div>
  <div class="hero-note">Jetzt neue Kollektion ansehen!<br>Bei der Hochzeitsmesse 23.–25. März in Mainz</div>
  <span class="hero-arrow prev"><svg width="12" height="12" viewBox="0 0 12 12"><path d="M8 1 3 6l5 5" fill="none" stroke="#fff" stroke-width="2"/></svg></span>
  <span class="hero-arrow next"><svg width="12" height="12" viewBox="0 0 12 12"><path d="M4 1l5 5-5 5" fill="none" stroke="#fff" stroke-width="2"/></svg></span>
</section>

<main class="container">
  <section class="info">
    <h2 class="section-title">Informationen</h2>
    <div class="title-rule"></div>
    <div class="info-row">
      <p>Lorem ipsum dolor sit amet, consectetur adipiscing elit, sed do eiusmod tempor incididunt ut labore et dolore magna aliqua. Ut enim ad minim veniam, quis nostrud exercitation ullamco laboris nisi ut aliquip ex ea commodo consequat. Duis aute irure dolor in reprehenderit in voluptate velit esse cillum dolore eu fugiat nulla pariatur, excepteur sint occaecat cupidatat non proident, sunt in culpa qui officia deserunt mollit anim.</p>
      <div class="partner-badge"></div>
    </div>
  </section>

  <h2 class="edition-title">Edition 1</h2>
  <div class="edition-rule"></div>
  <div class="card-grid">
    <article class="ring-card"><div class="ring-photo photo-gold" role="img" aria-label="Zwei Trauringe in Gelbgold"></div><ul class="ring-specs"><li>333/14 Gelbgold</li><li>1 Brillant</li><li>0,03 Carat</li></ul><span class="btn-request">Preisanfrage</span></article>
    <article class="ring-card"><div class="ring-photo photo-bicolor" role="img" aria-label="Zwei Trauringe in Gelb- und Weißgold"></div><ul class="ring-specs"><li>585/14 Gelbgold/Weißgold</li><li>7 Brillanten</li><li>0,08 Carat</li></ul><span class="btn-request">Preisanfrage</span></article>
    <article class="ring-card"><div class="ring-photo photo-white" role="img" aria-label="Zwei Trauringe in Weißgold"></div><ul class="ring-specs"><li>585/14 Weißgold, Palladium, Platin</li><li>3 Brillanten</li></ul><span class="btn-request">Preisanfrage</span></article>
  </div>

  <h2 class="edition-title">Edition 2</h2>
  <div class="edition-rule"></div>
  <div class="card-grid">
    <article class="ring-card"><div class="ring-photo photo-gold" role="img" aria-label="Zwei Trauringe in Gelbgold"></div><ul class="ring-specs"><li>333/14 Gelbgold</li><li>1 Brillant</li><li>0,03 Carat</li></ul><span class="btn-request">Preisanfrage</span></article>
    <article class="ring-card"><div class="ring-photo photo-bicolor" role="img" aria-label="Zwei Trauringe in Gelb- und Weißgold"></div><ul class="ring-specs"><li>585/14 Gelbgold/Weißgold</li><li>7 Brillanten</li><li>0,08 Carat</li></ul><span class="btn-request">Preisanfrage</span></article>
    <article class="ring-card"><div class="ring-photo photo-white" role="img" aria-label="Zwei Trauringe in Weißgold"></div><ul class="ring-specs"><li>585/14 Weißgold, Palladium, Platin</li><li>3 Brillanten</li><li>0,08 Carat</li></ul><span class="btn-request">Preisanfrage</span></article>
  </div>

  <section class="design-banner" role="img" aria-label="Dunkles Foto einer Werkstatt mit Trauringen">
    <div class="banner-text">
      <h3>Trauringe kolbeck gestalten</h3>
      <p>Lorem ipsum dolor sit amet, consectetur adipiscing elit. Gestalten Sie Ihre Trauringe ganz nach Ihren Wünschen im Konfigurator und fragen Sie unverbindlich Ihr persönliches Angebot an.</p>
      <span class="btn-request">Preisanfrage</span>
    </div>
    <div class="banner-video" role="img" aria-label="Vorschau des Ring-Konfigurators mit zwei Ringen"></div>
  </section>

  <h2 class="edition-title">Exclusive</h2>
  <div class="edition-rule"></div>
  <div class="card-grid">
    <article class="ring-card"><div class="ring-photo photo-gold" role="img" aria-label="Zwei Trauringe in Gelbgold"></div><ul class="ring-specs"><li>333/14 Gelbgold</li><li>1 Brillant</li><li>0,03 Carat</li></ul><span class="btn-request">Preisanfrage</span></article>
    <article class="ring-card"><div class="ring-photo photo-bicolor" role="img" aria-label="Zwei Trauringe in Gelb- und Weißgold"></div><ul class="ring-specs"><li>585/14 Gelbgold/Weißgold</li><li>7 Brillanten</li><li>0,08 Carat</li></ul><span class="btn-request">Preisanfrage</span></article>
    <article class="ring-card"><div class="ring-photo photo-white" role="img" aria-label="Zwei Trauringe in Weißgold"></div><ul class="ring-specs"><li>585/14 Weißgold, Palladium, Platin</li><li>3 Brillanten</li></ul><span class="btn-request">Preisanfrage</span></article>
  </div>
</main>

<footer>
  <div class="site-footer">
    <div class="footer-brand">
      <div class="brand"><span class="brand-dot"></span><span>TRAURINGE<br>KOLBECK.DE</span></div>
      <div class="social-btn">Palvista</div>
    </div>
    <ul class="footer-col"><li>Trauringe Kolbeck</li><li>Edition 1</li><li>Edition 2</li><li>Exklusiv</li></ul>
    <ul class="footer-col"><li>Neu Edition</li><li>Konfigurator</li><li>Über uns</li><li>Kontakt</li></ul>
    <ul class="footer-col"><li>August Brennholt</li><li>Juwelier Kolbeck</li><li>Media</li><li>Mediathek</li></ul>
  </div>
  <div class="footer-bar">Trauringe Kolbeck GmbH · Lindenweg 12 · 55116 Musterstadt · Tel. 06131 555 010 · Fax 06131 555 011 · info@trauringe-kolbeck.de</div>
</footer>
</body>
</html>
```